Need a FLAT UI design for mobile campus Marketplace APP

We need to improve our current UI/UX design for a mobile application called Tradlo. It is designed for students to buy and sell their goods, such as books and furnitures, on their own campus to save living expenses. Our initial design does not look very flat and clear enough. We would like to see a flat design improvement for a better purchasing and selling experience using yellow as theme color.

Target Market(s)

college students

Industry/Entity Type

Marketplace

Colors
ffc214
ffcf3e
fee18a
fff3d1

Requirements
Must have
• an improved UI look, flat and simple.
Nice to have
• alternative designs
Should not have
• a new function design for the app on the design

```html
<!DOCTYPE html>
<html lang="en">
<head>
<meta charset="utf-8">
<title>Tradlo – Product Details</title>
<link href="https://fonts.googleapis.com/css2?family=Open+Sans:wght@400;500;600&display=swap" rel="stylesheet">
<style>
  :root {
    --page-bg: #f2f2f2;
    --theme-yellow: #ffcf3e;
    --theme-yellow-deep: #ffc214;
    --ink: #222428;
    --label-grey: #8a8d91;
    --bar-dark: #2d3238;
    --band-dark: rgba(45, 48, 52, 0.86);
    --like-red: #ef505c;
    --white: #ffffff;
  }
  * { box-sizing: border-box; margin: 0; padding: 0; }
  html, body {
    width: 1200px; height: 1111px; overflow: hidden;
    background: var(--page-bg);
    font-family: "Open Sans", Arial, sans-serif;
  }
  .screen {
    position: absolute; left: 320px; top: 58px;
    width: 560px; height: 995px;
    background: var(--white); overflow: hidden;
  }
  .app-header {
    position: absolute; left: 0; top: 0; width: 100%; height: 95px;
    background: var(--theme-yellow); color: var(--white);
  }
  .status-bar {
    position: absolute; left: 0; top: 0; width: 100%; height: 31px;
    display: flex; align-items: center; justify-content: space-between;
    padding: 0 10px; font-size: 16px;
  }
  .status-bar .battery { display: flex; align-items: center; gap: 5px; }
  .nav-bar { position: absolute; left: 0; top: 31px; width: 100%; height: 64px; }
  .nav-title {
    position: absolute; left: 0; width: 100%; top: 18px; text-align: center;
    font-size: 23px; font-weight: 600; letter-spacing: 0.3px;
  }
  .nav-back { position: absolute; left: 20px; top: 17px; }
  .nav-filter { position: absolute; left: 432px; top: 14px; }
  .nav-cart { position: absolute; left: 500px; top: 14px; }

  .product-photo {
    position: absolute; left: 0; top: 95px; width: 100%; height: 429px;
    background:
      linear-gradient(180deg, rgba(90,95,110,0.55) 0%, rgba(0,0,0,0) 25%),
      linear-gradient(100deg, #8a5a4a 0%, #b69a63 30%, #c7ad72 45%, #6b5b78 62%, #9a8a70 78%, #b8c4d6 100%);
  }
  .product-title {
    position: absolute; left: 23px; top: 120px;
    font-size: 35px; font-weight: 400; color: var(--white); letter-spacing: 0.4px;
  }
  .like-badge {
    position: absolute; left: 469px; top: 119px; width: 67px; height: 67px;
    border-radius: 50%; background: var(--like-red);
    display: flex; align-items: center; justify-content: center;
  }
  .seller-band {
    position: absolute; left: 0; top: 413px; width: 100%; height: 111px;
    background: var(--band-dark); color: var(--white);
  }
  .seller-avatar {
    position: absolute; left: 22px; top: 26px; width: 60px; height: 60px;
    border-radius: 50%; background: linear-gradient(135deg, #e9ddd4, #8c6f62);
    border: 2px solid var(--white);
  }
  .seller-name { position: absolute; left: 97px; top: 24px; font-size: 26px; font-weight: 500; letter-spacing: -0.2px; }
  .seller-time {
    position: absolute; left: 97px; top: 62px; font-size: 17px;
    display: flex; align-items: center; gap: 6px;
  }
  .send-message {
    position: absolute; left: 345px; top: 31px; width: 191px; height: 51px;
    border-radius: 26px; background: var(--theme-yellow);
    color: var(--white); font-size: 17px; font-weight: 600;
    display: flex; align-items: center; justify-content: center;
  }
  .details { position: absolute; left: 24px; top: 524px; right: 18px; color: var(--ink); }
  .field-label {
    font-size: 17px; font-weight: 600; color: var(--label-grey);
    letter-spacing: 0.4px; margin-top: 32px;
  }
  .description { font-size: 24px; line-height: 33px; margin-top: 14px; letter-spacing: -0.3px; }
  .price { font-size: 24px; margin-top: 15px; }
  .price-label { margin-top: 32px; }

  .tab-bar {
    position: absolute; left: 0; top: 908px; width: 100%; height: 87px;
    display: flex; background: var(--bar-dark);
  }
  .tab { flex: 1; display: flex; align-items: center; justify-content: center; }
  .tab.is-active { background: var(--theme-yellow); }
</style>
</head>
<body>
<main class="screen">
  <header class="app-header">
    <div class="status-bar">
      <span>●●●●● Campus</span>
      <span>9:41 AM</span>
      <span class="battery">42%
        <svg width="30" height="13" viewBox="0 0 30 13"><rect x="0.5" y="0.5" width="26" height="12" rx="2" fill="none" stroke="#fff"/><rect x="2" y="2" width="10" height="9" fill="#fff"/><rect x="27.5" y="4" width="2" height="5" fill="#fff"/></svg>
      </span>
    </div>
    <nav class="nav-bar">
      <svg class="nav-back" width="18" height="32" viewBox="0 0 18 32"><path d="M16 2 L2 16 L16 30" fill="none" stroke="#fff" stroke-width="2.5"/></svg>
      <div class="nav-title">PRODUCT DETAILS</div>
      <svg class="nav-filter" width="38" height="36" viewBox="0 0 38 36" fill="none" stroke="#fff" stroke-width="2">
        <line x1="6" y1="2" x2="6" y2="22"/><circle cx="6" cy="27" r="4"/><line x1="6" y1="31" x2="6" y2="34"/>
        <line x1="19" y1="2" x2="19" y2="6"/><circle cx="19" cy="11" r="4"/><line x1="19" y1="15" x2="19" y2="34"/>
        <line x1="32" y1="2" x2="32" y2="22"/><circle cx="32" cy="27" r="4"/><line x1="32" y1="31" x2="32" y2="34"/>
      </svg>
      <svg class="nav-cart" width="36" height="36" viewBox="0 0 36 36" fill="none" stroke="#fff" stroke-width="2">
        <path d="M1 4 H7 L11 24 H31 L34 9 H8"/><circle cx="13" cy="31" r="3"/><circle cx="29" cy="31" r="3"/>
      </svg>
    </nav>
  </header>

  <div class="product-photo" role="img" aria-label="Photo of the listed item: a furnished living room with striped sofa, lamp and tall windows"></div>
  <h1 class="product-title">Maple Desk Set</h1>
  <div class="like-badge">
    <svg width="34" height="30" viewBox="0 0 56 50"><path d="M28 46 C10 32 3 24 3 15 C3 8 8 3 15 3 C21 3 25 6 28 10 C31 6 35 3 41 3 C48 3 53 8 53 15 C53 24 46 32 28 46Z" fill="#fff"/></svg>
  </div>

  <section class="seller-band">
    <div class="seller-avatar" role="img" aria-label="Seller profile photo"></div>
    <div class="seller-name">Nora Pellam</div>
    <div class="seller-time">
      <svg width="17" height="17" viewBox="0 0 17 17" fill="none" stroke="#fff" stroke-width="1.5"><circle cx="8.5" cy="8.5" r="7.3"/><path d="M8.5 4 V8.5 H12"/></svg>
      Yesterday
    </div>
    <div class="send-message">SEND MESSAGE</div>
  </section>

  <section class="details">
    <p class="field-label">DESCRIPTION</p>
    <p class="description">A sturdy desk set that can either be painted or kept, this is a set that can be used as a study corner for years. In good shape.</p>
    <p class="field-label price-label">PRICE</p>
    <p class="price">$450.00</p>
  </section>

  <nav class="tab-bar">
    <div class="tab">
      <svg width="50" height="48" viewBox="0 0 50 48" fill="none" stroke="#fff" stroke-width="2.2"><path d="M25 3 A21 19 0 1 1 14 39 L4 44 L8 35 A21 19 0 0 1 25 3Z"/><circle cx="17" cy="22" r="1.6" fill="#fff"/><circle cx="25" cy="22" r="1.6" fill="#fff"/><circle cx="33" cy="22" r="1.6" fill="#fff"/></svg>
    </div>
    <div class="tab is-active">
      <svg width="52" height="46" viewBox="0 0 56 50" fill="none" stroke="#fff" stroke-width="2.8"><path d="M28 46 C10 32 3 24 3 15 C3 8 8 3 15 3 C21 3 25 6 28 10 C31 6 35 3 41 3 C48 3 53 8 53 15 C53 24 46 32 28 46Z"/></svg>
    </div>
    <div class="tab">
      <svg width="56" height="50" viewBox="0 0 56 50"><rect x="2" y="4" width="52" height="30" rx="4" fill="#fff"/><rect x="6" y="9" width="44" height="20" rx="3" fill="#2d3238"/><text x="28" y="22.5" text-anchor="middle" font-family="Open Sans, sans-serif" font-size="7.5" font-weight="600" fill="#fff">RESERVED</text><path d="M28 34 V46 M18 46 H38 M22 40 H34" stroke="#fff" stroke-width="2.5"/></svg>
    </div>
  </nav>
</main>
</body>
</html>
```